business card for a massage therapy practice named 'Meadow and Willow Massage Studio'

I really need a trendy, yet easy on the eyes business card to complement my logo. Ideally with some gold or rose gold foil work.

My uploaded file of the logo I have in horizontal but I have a vertical version as well. Another color that is used in the website is a blush pink here and there. I'd like to see some trendy tropical leaves in the design.

```html
<!DOCTYPE html>
<html lang="en">
<head>
<meta charset="utf-8">
<title>Meadow and Willow Massage Studio – Business Card</title>
<link rel="stylesheet" href="https://fonts.googleapis.com/css2?family=Kaushan+Script&family=Work+Sans:wght@400&display=swap">
<style>
  :root {
    --page-bg: #dfe3e8;
    --card-bg: #f1f3f6;
    --gold-dark: #6f5f40;
    --gold-light: #8c7a55;
    --band-dark: #1f1f1f;
    --ink: #2a2a28;
    --rule: #5b5a55;
    --accent: #a38f62;
  }
  * { margin: 0; padding: 0; box-sizing: border-box; }
  html, body { width: 1200px; height: 900px; overflow: hidden; }
  body { background: var(--page-bg); position: relative; font-family: "Work Sans", sans-serif; }

  .card {
    position: absolute; left: 100px; top: 166px;
    width: 1000px; height: 569px;
    background: var(--card-bg);
    overflow: hidden;
    box-shadow: 0 10px 30px rgba(0,0,0,0.15);
  }
  .card-header-band {
    position: absolute; left: 0; top: 0; width: 1000px; height: 120px;
    background: linear-gradient(180deg, var(--gold-light) 0%, var(--gold-dark) 78%, var(--band-dark) 100%);
  }

  .brand {
    position: absolute; left: 52px; top: 165px;
    display: flex; align-items: center; gap: 18px;
    font-family: "Work Sans", sans-serif; font-weight: 400; color: var(--ink);
  }
  .brand-dot { width: 48px; height: 48px; border-radius: 50%; background: var(--accent); flex: none; }
  .brand-name { font-size: 30px; line-height: 1.2; }

  .holder-name {
    position: absolute; right: 49px; top: 300px;
    font-family: "Kaushan Script", cursive; font-size: 54px; font-weight: 400; color: var(--ink);
  }
  .divider { position: absolute; left: 49px; right: 49px; top: 398px; height: 2px; background: var(--rule); }

  .contact-list { position: absolute; left: 49px; top: 440px; list-style: none; }
  .contact-list li { display: flex; align-items: center; gap: 10px; height: 31px; font-size: 21px; color: var(--ink); }
  .contact-list svg { width: 15px; height: 15px; flex: none; }

  .address {
    position: absolute; right: 49px; top: 471px;
    text-align: right; font-size: 21px; line-height: 31px; color: var(--ink); font-style: normal;
  }
</style>
</head>
<body>
  <section class="card" aria-label="Business card">
    <div class="card-header-band" role="img" aria-label="Gold foil and black decorative wave band across the top of the card"></div>

    <div class="brand">
      <span class="brand-dot"></span>
      <div class="brand-name">Meadow and Willow<br>Massage Studio</div>
    </div>

    <h1 class="holder-name">Marisol Vega</h1>
    <div class="divider"></div>

    <ul class="contact-list">
      <li>
        <svg viewBox="0 0 16 16" aria-hidden="true"><path d="M4 1.5 L6 4.5 L4.8 6 C5.6 8 7.5 10 10 11.2 L11.5 10 L14.5 12 L13 14.5 C7 14 2 9 1.5 3 Z" fill="none" stroke="var(--ink)" stroke-width="1.2"/></svg>
        <span>(555) 214-7730</span>
      </li>
      <li>
        <svg viewBox="0 0 16 16" aria-hidden="true"><rect x="1.5" y="3.5" width="13" height="9" fill="none" stroke="var(--ink)" stroke-width="1.2"/><path d="M1.5 3.5 L8 9 L14.5 3.5" fill="none" stroke="var(--ink)" stroke-width="1.2"/></svg>
        <span>meadowandwillow@gmail.com</span>
      </li>
      <li>
        <svg viewBox="0 0 16 16" aria-hidden="true"><circle cx="8" cy="8" r="6.5" fill="none" stroke="var(--ink)" stroke-width="1.2"/><path d="M1.5 8 H14.5 M8 1.5 C5 5 5 11 8 14.5 M8 1.5 C11 5 11 11 8 14.5" fill="none" stroke="var(--ink)" stroke-width="1.1"/></svg>
        <span>meadowandwillow.com</span>
      </li>
    </ul>

    <address class="address">418 Linden Ave. suite 210,<br>Fairview, CA 95000</address>
  </section>
</body>
</html>
```